Business Card Design

After a corporate career in the finance sector I am now operating on my own as a consultant. I require a simple design, and want a strong card which is targeted at a conservative audience.

Target Market(s)

highly educated senior management, directors of companies, finance sector

Industry/Entity Type

Conservative

Contact Information for Business Card

Ruth Danver
Consultant
Mobile: 0417 862 450
Email: ruth.danv@mailcove.net

Requirements
Should not have
• I don't want the colours green/yellow/brown

```html
<!DOCTYPE html>
<html lang="en">
<head>
<meta charset="utf-8">
<title>Ruth Danver – Consultant Business Card</title>
<link rel="stylesheet" href="https://fonts.googleapis.com/css2?family=Open+Sans:wght@400;600;700&display=swap">
<style>
  :root {
    --page-bg: #e9e9e7;
    --card-black: #070707;
    --band-white: #efeced;
    --name-ink: #1a1a1a;
    --contact-grey: #6f6f6f;
    --card-shadow: rgba(0, 0, 0, 0.28);
  }

  html, body {
    margin: 0;
    padding: 0;
    width: 1200px;
    height: 750px;
    overflow: hidden;
    background: var(--page-bg);
  }

  .stage {
    position: relative;
    width: 1200px;
    height: 750px;
  }

  .business-card {
    position: absolute;
    left: 180px;
    top: 135px;
    width: 840px;
    height: 480px;
    background: var(--card-black);
    box-shadow: 0 14px 36px var(--card-shadow);
    font-family: "Open Sans", Arial, sans-serif;
    overflow: hidden;
  }

  .name-band {
    position: absolute;
    left: 0;
    top: 182px;
    width: 480px;
    height: 58px;
    background: var(--band-white);
    display: flex;
    align-items: center;
    justify-content: flex-end;
    padding-right: 40px;
    box-sizing: border-box;
    color: var(--name-ink);
    white-space: nowrap;
  }

  .holder-name {
    font-size: 23px;
    font-weight: 600;
    letter-spacing: 0.2px;
  }

  .divider {
    font-size: 24px;
    font-weight: 400;
    margin: 0 7px;
  }

  .holder-title {
    font-size: 16px;
    font-weight: 400;
  }

  .contact-line {
    position: absolute;
    right: 30px;
    top: 356px;
    margin: 0;
    font-size: 16px;
    color: var(--contact-grey);
    white-space: nowrap;
    letter-spacing: 0.2px;
  }

  .contact-label {
    font-weight: 700;
  }

  .contact-sep {
    margin: 0 4px;
  }
</style>
</head>
<body>
  <main class="stage">
    <section class="business-card" aria-label="Business card for Ruth Danver, Consultant">
      <div class="name-band">
        <span class="holder-name">Ruth Danver</span>
        <span class="divider">|</span>
        <span class="holder-title">Consultant</span>
      </div>
      <p class="contact-line">
        <span class="contact-label">Ph :</span> 0417 862 450
        <span class="contact-sep">|</span>
        <span class="contact-label">Mail :</span> ruth.danv@mailcove.net
      </p>
    </section>
  </main>
</body>
</html>
```